Construction Company Website

I need a website for my construction company
Target Market(s)
People looking for construction work
Coding
Coded - Design and coding required
Number of Pages Required
4 page
Colors
0455a3
ffc214
Requirements
Must have
- A home page about my company,
A completed projects page showcasing some completed works
A contact me page with an enquiry form
Nice to have
- Professional and contemporary whilst classy website.

```html
<!DOCTYPE html>
<html lang="en">
<head>
<meta charset="utf-8">
<title>Halden Build – Groundworks, Landscaping, Extensions</title>
<link href="https://fonts.googleapis.com/css2?family=Mulish:wght@400;600;700&display=swap" rel="stylesheet">
<style>
:root{
  --navy:#0f1b33;
  --blue:#0b47a3;
  --blue-deep:#083a88;
  --gold:#ffc214;
  --ink:#1b2440;
  --grey:#efefef;
  --text:#4a4a4a;
  --white:#fff;
}
*{box-sizing:border-box;margin:0;padding:0}
html,body{width:1200px;height:3959px;overflow:hidden}
body{position:relative;font-family:"Mulish",sans-serif;color:var(--text);background:var(--white)}
.abs{position:absolute}
svg{display:block}
.btn{position:absolute;display:flex;align-items:center;justify-content:center;font-size:15px;border-radius:2px}
.btn--blue{background:var(--blue);color:var(--white)}
.btn--gold{background:var(--gold);color:var(--ink)}
.photo{position:absolute}

/* header */
.site-header{left:0;top:0;width:1200px;height:160px;background:var(--navy)}
.brand{left:144px;top:48px;display:flex;align-items:center;gap:12px}
.brand__mark{width:34px;height:34px;background:var(--gold)}
.brand__name{color:var(--gold);font-size:24px;font-weight:600;letter-spacing:2px}
.phone{right:144px;top:44px;color:var(--white);font-size:25px;font-weight:600;display:flex;align-items:center;gap:12px}
.nav{right:144px;top:116px;display:flex;gap:42px;font-size:16px;color:var(--white)}
.nav .is-active{color:var(--gold)}

/* hero */
.hero{left:0;top:160px;width:1200px;height:600px}
.hero__title{left:144px;color:var(--white);font-size:34px;font-weight:600;line-height:40px}
.arrow{position:absolute;width:44px;height:44px;border-radius:50%;background:var(--navy);display:flex;align-items:center;justify-content:center}

/* welcome */
.welcome__title{left:622px;top:904px;font-size:33px;color:var(--blue);font-weight:600}
.welcome__text{left:622px;top:960px;width:434px;font-size:13.5px;line-height:27.3px}

/* sections */
.band{left:0;width:1200px;background:linear-gradient(180deg,var(--blue),var(--blue-deep))}
.h2{position:absolute;left:0;width:1200px;text-align:center;font-size:33px;font-weight:600}
.service__name{position:absolute;top:1854px;width:256px;text-align:center;font-size:33px;line-height:40px;color:var(--gold)}
.service__text{position:absolute;top:1900px;width:260px;text-align:center;font-size:11.5px;line-height:22px;color:var(--white);letter-spacing:-0.1px}

.testimonial{left:144px;top:2226px;width:912px;height:255px;background:var(--grey)}
.testimonial__text{left:647px;top:2256px;width:400px;font-size:16.5px;line-height:30.5px;color:var(--ink)}
.testimonial__name{left:647px;top:2422px;font-size:16px;color:var(--blue);font-weight:600}
.dots{left:508px;top:2509px;display:flex;gap:20px}
.dots span{width:12px;height:12px;border-radius:50%;background:#999}
.dots span.is-active{background:var(--blue)}

.field{position:absolute;border-bottom:1.5px solid var(--ink);font-size:16px;color:var(--ink);padding:0 12px 6px}

.footer-links{left:0;width:1200px;top:3870px;text-align:center;font-size:11.5px;color:var(--white)}
.footer-copy{left:0;width:1200px;top:3904px;text-align:center;font-size:11.5px;color:var(--white)}
.social{position:absolute;top:3792px;width:48px;height:48px;border-radius:50%;border:1.5px solid var(--white)}
</style>
</head>
<body>

<header class="abs site-header">
  <div class="abs brand"><span class="brand__mark"></span><span class="brand__name">HALDEN BUILD</span></div>
  <div class="abs phone">
    <svg width="22" height="22" viewBox="0 0 24 24"><path fill="#fff" d="M6.6 10.8a15 15 0 0 0 6.6 6.6l2.2-2.2a1 1 0 0 1 1-.25 11 11 0 0 0 3.6.6 1 1 0 0 1 1 1V20a1 1 0 0 1-1 1A17 17 0 0 1 3 4a1 1 0 0 1 1-1h3.5a1 1 0 0 1 1 1c0 1.25.2 2.45.6 3.6a1 1 0 0 1-.25 1z"/></svg>
    07700 900123
  </div>
  <nav class="abs nav"><span class="is-active">HOME</span><span>ABOUT US</span><span>SERVICES</span><span>PROJECTS</span><span>CONTACT US</span></nav>
</header>

<section class="abs hero">
  <svg width="1200" height="600" viewBox="0 0 1200 600" role="img" aria-label="Photo of a construction site with a newly laid patio base and a parked truck">
    <defs><linearGradient id="heroGrad" x1="0" y1="0" x2="0" y2="1"><stop offset="0" stop-color="#8d9098"/><stop offset="0.35" stop-color="#7b6f5f"/><stop offset="1" stop-color="#a58c75"/></linearGradient></defs>
    <polygon points="0,0 1200,0 1200,455 600,583 0,455" fill="url(#heroGrad)"/>
    <polygon points="0,455 600,583 1200,455 1200,463 600,595 0,463" fill="#ffc214"/>
  </svg>
  <h1 class="abs hero__title" style="top:158px">VESTIBULUM&nbsp; PLACERAT<br>RISUS POSUERE</h1>
  <span class="btn btn--blue" style="left:144px;top:247px;width:111px;height:40px">Read More</span>
  <span class="arrow" style="left:55px;top:204px"><svg width="14" height="20"><path d="M11 2 3 10l8 8" stroke="#fff" stroke-width="3" fill="none"/></svg></span>
  <span class="arrow" style="left:1099px;top:204px"><svg width="14" height="20"><path d="m3 2 8 8-8 8" stroke="#fff" stroke-width="3" fill="none"/></svg></span>
</section>

<section>
  <svg class="photo" style="left:144px;top:837px" width="420" height="487" viewBox="0 0 420 487" role="img" aria-label="Photo of a brick house with a conservatory and stacked timber on the lawn">
    <defs><linearGradient id="welGrad" x1="0" y1="0" x2="0" y2="1"><stop offset="0" stop-color="#a2553c"/><stop offset="0.55" stop-color="#c9cfd3"/><stop offset="1" stop-color="#6e8a3e"/></linearGradient></defs>
    <polygon points="210,0 420,122 420,365 210,487 0,365 0,122" fill="url(#welGrad)"/>
    <path d="M0 125 210 245 420 125M210 245V487" stroke="#fff" stroke-width="12" fill="none"/>
  </svg>
  <h2 class="abs welcome__title">Welcome to Halden Build</h2>
  <p class="abs welcome__text">Maecenas vel tortor accumsan quam varius imperdiet vel eget elit. Aenean facilisis tincidunt lectus, id dictum nisi luctus eget. Vivamus efficitur ex condimentum, malesuada eros eget, feugiat nibh. Sed tellus ex, imperdiet eget gravida sit amet, volutpat eget turpis. In nec ultricies est. Etiam mattis augue vehicula odio posuere, sit amet tempus lectus luctus. Nulla facilisi. Etiam vel massa elementum, bibendum tellus venenatis, feugiat massa. Curabitur venenatis lacinia ornare. Cras sollicitudin cursus dui eu placerat.</p>
  <span class="btn btn--blue" style="left:622px;top:1201px;width:112px;height:39px">Read More</span>
</section>

<section class="abs band" style="top:1404px;height:695px"></section>
<h2 class="h2" style="top:1474px;color:var(--white)">Services</h2>

<svg class="photo" style="left:144px;top:1541px" width="256" height="293" viewBox="0 0 256 293" role="img" aria-label="Photo of groundworks with stacked timber beside a house"><polygon points="128,0 256,73 256,220 128,293 0,220 0,73" fill="#a58466"/></svg>
<div class="service__name" style="left:144px">Groundworks</div>
<p class="service__text" style="left:142px">Vivamus lacus justo, ultrices nec erat in, euismod iaculis mauris. Vivamus eleifend vitae nulla vel malesuada. In ac malesuada lacus.</p>

<svg class="photo" style="left:472px;top:1541px" width="256" height="293" viewBox="0 0 256 293" role="img" aria-label="Photo of a landscaped garden with artificial lawn and timber edging"><polygon points="128,0 256,73 256,220 128,293 0,220 0,73" fill="#5e9a3a"/></svg>
<div class="service__name" style="left:472px">Landscaping</div>
<p class="service__text" style="left:470px">Vivamus lacus justo, ultrices nec erat in, euismod iaculis mauris. Vivamus eleifend vitae nulla vel malesuada. In ac malesuada lacus.</p>

<svg class="photo" style="left:800px;top:1541px" width="256" height="293" viewBox="0 0 256 293" role="img" aria-label="Photo of grey composite decking beside a brick extension"><polygon points="128,0 256,73 256,220 128,293 0,220 0,73" fill="#8a8d92"/></svg>
<div class="service__name" style="left:800px">Extensions</div>
<p class="service__text" style="left:798px">Vivamus lacus justo, ultrices nec erat in, euismod iaculis mauris. Vivamus eleifend vitae nulla vel malesuada. In ac malesuada lacus.</p>

<span class="btn btn--gold" style="left:216px;top:1980px;width:112px;height:37px">Read More</span>
<span class="btn btn--gold" style="left:544px;top:1980px;width:112px;height:37px">Read More</span>
<span class="btn btn--gold" style="left:872px;top:1980px;width:112px;height:37px">Read More</span>

<h2 class="h2" style="top:2168px;color:var(--ink)">Testimonials</h2>
<div class="abs testimonial"></div>
<svg class="photo" style="left:144px;top:2226px" width="456" height="255" role="img" aria-label="Photo of a new slate front path beside a brick house"><rect width="456" height="255" fill="#6f6b68"/></svg>
<svg class="photo" style="left:580px;top:2333px" width="40" height="40" viewBox="0 0 40 40"><circle cx="20" cy="20" r="20" fill="#ffc214"/><path d="M12 24v-4c0-3 2-5 4-5v2c-1 0-2 1-2 3h2v4zM21 24v-4c0-3 2-5 4-5v2c-1 0-2 1-2 3h2v4z" fill="#1b2440"/></svg>
<p class="abs testimonial__text">Vivamus lacus justo, ultrices erat in, euismod iaculis mauris. Vivamus eleifend vitae nulla malesuada. In ac malesuada lacus, et consectetur ante. Fusce vitae lectus sit amet pulvinar maximus. Aenean placerat, nibh vel accumsan aliquet.</p>
<p class="abs testimonial__name">- Mara Fenwick, City</p>
<div class="abs dots"><span class="is-active"></span><span></span><span></span><span></span><span></span><span></span></div>

<section class="abs band" style="top:2602px;height:667px"></section>
<h2 class="h2" style="top:2672px;color:var(--white)">Projects</h2>
<svg class="photo" style="left:144px;top:2739px" width="450" height="450" role="img" aria-label="Photo of a finished play area with timber fencing and a new lawn"><rect width="450" height="450" fill="#6d8a5a"/></svg>
<svg class="photo" style="left:604px;top:2739px" width="452" height="219" role="img" aria-label="Photo of a garden room with decking and a pool cover"><rect width="452" height="219" fill="#8d8c80"/></svg>
<svg class="photo" style="left:604px;top:2969px" width="221" height="220" role="img" aria-label="Photo of a renovated interior room with a red wall"><rect width="221" height="220" fill="#a46262"/></svg>
<svg class="photo" style="left:834px;top:2969px" width="222" height="220" role="img" aria-label="Photo of a paved garden patio with lawn"><rect width="222" height="220" fill="#7c8765"/></svg>
<svg class="photo" style="left:65px;top:2952px" width="24" height="26"><path d="M16 3 6 13l10 10" stroke="#fff" stroke-width="3" fill="none"/></svg>
<svg class="photo" style="left:1110px;top:2952px" width="24" height="26"><path d="m8 3 10 10-10 10" stroke="#fff" stroke-width="3" fill="none"/></svg>

<h2 class="h2" style="top:3338px;color:var(--ink)">Contact Us</h2>
<div class="field" style="left:144px;top:3406px;width:289px">First Name</div>
<div class="field" style="left:455px;top:3406px;width:290px">Last Name</div>
<div class="field" style="left:767px;top:3406px;width:289px">Email Address</div>
<div class="field" style="left:144px;top:3478px;width:289px">Phone Number</div>
<div class="field" style="left:455px;top:3478px;width:290px">Address</div>
<div class="field" style="left:767px;top:3478px;width:289px;display:flex;justify-content:space-between">Service for <svg width="14" height="10" style="margin-top:6px"><path d="m1 2 6 6 6-6" stroke="#1b2440" stroke-width="2" fill="none"/></svg></div>
<div class="field" style="left:144px;top:3550px;width:912px">Message</div>
<span class="btn btn--gold" style="left:556px;top:3606px;width:88px;height:38px">Submit</span>

<footer>
  <svg class="photo" style="left:0;top:3720px" width="1200" height="239" viewBox="0 0 1200 239">
    <polygon points="0,135 600,5 1200,135 1200,239 0,239" fill="#ffc214"/>
    <polygon points="0,145 600,17 1200,145 1200,239 0,239" fill="#0f1b33"/>
  </svg>
  <span class="social" style="left:540px" aria-label="Social link"></span>
  <span class="social" style="left:612px" aria-label="Social link"></span>
  <p class="abs footer-links">Home &nbsp;&nbsp;|&nbsp;&nbsp; About Us &nbsp;&nbsp;|&nbsp;&nbsp; Services &nbsp;&nbsp;|&nbsp;&nbsp; Projects &nbsp;&nbsp;|&nbsp;&nbsp; Contact Us</p>
  <p class="abs footer-copy">Copyright © 2020 Halden Build. &nbsp;All rights reserved.</p>
</footer>

</body>
</html>
```